help me Create Brightfern Catering offsite menus

I need something vibrant and it needs some pictures to go with the food i will include the logo of the location and the menu. it is for offsite catering to be delivered to venues in our local town, we are currently catering in house only but are expanding to do delivery so need something that i can use as a menu. the file needs to be able to be edited

Target Market(s)

local small businesses that require catering for their group lunches

Industry/Entity Type

Catering

Font styles to use
Serif
Decorative

Requirements
Must have
• colour and soul, must have a good feeling and be happy
Nice to have
• some other stock photos of the described products
Should not have
• not be too corporate and businessy

```html
<!DOCTYPE html>
<html lang="en">
<head>
<meta charset="utf-8">
<title>Brightfern Catering – Conference Menu</title>
<link href="https://fonts.googleapis.com/css2?family=Tinos&family=Didact+Gothic&family=Pathway+Gothic+One&display=swap" rel="stylesheet">
<style>
  :root {
    --bg: #0b1a26;
    --divider: #22384a;
    --ink: #f4f1ea;
    --price: #e8792b;
  }
  * { margin: 0; padding: 0; box-sizing: border-box; }
  html, body { width: 848px; height: 1200px; overflow: hidden; background: var(--bg); }
  .menu {
    position: relative; width: 848px; height: 1200px; background: var(--bg);
    color: var(--ink); font-family: "Tinos", "Times New Roman", serif;
    font-size: 18px; line-height: 22.4px;
  }
  .rule-v { position: absolute; top: 0; bottom: 0; border-left: 1px dashed var(--divider); }
  .rule-v.one { left: 284px; }
  .rule-v.two { left: 566px; }
  .rule-h { position: absolute; left: 0; right: 0; top: 606px; border-top: 1px solid var(--divider); }

  .heading {
    position: absolute; font-family: "Didact Gothic", "Century Gothic", sans-serif;
    font-size: 20px; line-height: 28px; letter-spacing: 0.5px; text-align: center; font-weight: 400;
  }
  .item {
    position: absolute; white-space: nowrap;
    transform: scaleX(0.86); transform-origin: left top;
  }
  .price { color: var(--price); }

  .artwork { position: absolute; }
  .chef-cat { left: 36px; top: 62px; width: 208px; height: 210px; border-radius: 44% 44% 30% 30%;
    background: radial-gradient(circle at 55% 40%, #f08c3c 0%, #e07530 55%, #b85a2a 100%); }
  .teacup { left: 328px; top: 360px; width: 160px; height: 184px; border-radius: 40% 40% 50% 50%;
    background: radial-gradient(circle at 50% 55%, #e8e46a 0%, #d4cf4a 55%, #8f8a28 100%); }
  .sandwich { left: 632px; top: 854px; width: 148px; height: 118px; border-radius: 30%;
    background: linear-gradient(160deg, #e8a46a, #d9573a 60%, #8cae3c); }
  .pizza { left: 320px; top: 1052px; width: 192px; height: 70px; border-radius: 12px 12px 90px 90px;
    background: radial-gradient(circle at 50% 40%, #f2a03e 0%, #e06a2c 70%, #b8482a 100%); }

  .brand-name {
    position: absolute; left: 36px; width: 212px; top: 334px; text-align: center;
    font-family: "Tinos", serif; font-size: 26px; line-height: 30px; color: var(--ink);
  }
  .title {
    position: absolute; left: 0; width: 288px; top: 432px; text-align: center; font-weight: 400;
    font-family: "Pathway Gothic One", "Oswald", sans-serif; font-size: 29px; line-height: 34px;
  }
  .title-line { position: absolute; height: 2px; background: var(--ink); }
  .booking { position: absolute; left: 603px; top: 1079px; font-size: 15px; line-height: 21px;
    white-space: nowrap; transform: scaleX(0.86); transform-origin: left top; }
</style>
</head>
<body>
<main class="menu">
  <div class="rule-v one"></div>
  <div class="rule-v two"></div>
  <div class="rule-h"></div>

  <!-- Brand panel -->
  <div class="artwork chef-cat" role="img" aria-label="Illustration of a chef character in a hat and apron holding a plate of cupcakes"></div>
  <p class="brand-name">Brightfern<br>Catering</p>
  <h1 class="title">CONFERENCE MENU</h1>
  <div class="title-line" style="left:57px; top:469px; width:174px;"></div>
  <div class="title-line" style="left:77px; top:483px; width:134px;"></div>

  <!-- Tea & coffee -->
  <h2 class="heading" style="left:284px; width:250px; top:34px;">TEA &amp; COFFEE</h2>
  <p class="item" style="left:329px; top:79px;">Tea and coffee station<br><span class="price">$3.00 pp</span></p>
  <p class="item" style="left:329px; top:131px;">Continuous tea and<br>coffee enough to serve<br>for the day &nbsp;&nbsp;&nbsp;&nbsp;<span class="price">$5.00</span></p>
  <p class="item" style="left:329px; top:208px;">Barrista delivered<br>&nbsp;(pre order only)<br>&nbsp;&nbsp;&nbsp;<span class="price">$5.50 each</span></p>
  <h2 class="heading" style="left:334px; width:176px; top:289px;">EXTRAS</h2>
  <p class="item" style="left:329px; top:327px;">Juice 2 Lt Bottle<br><span class="price">$3.95</span></p>
  <div class="artwork teacup" role="img" aria-label="Illustration of a yellow cup of tea with steam and a wrapped sweet"></div>

  <!-- Morning or afternoon tea -->
  <h2 class="heading" style="left:600px; width:216px; top:30px;">Morning or<br>afternoon Tea</h2>
  <p class="item" style="left:622px; top:93px;">Scones and slices platter<br>&nbsp;&nbsp;&nbsp;&nbsp;&nbsp;&nbsp;&nbsp;<span class="price">$6.50per person</span></p>
  <p class="item" style="left:624px; top:146px;">Muffins<br><span class="price">$5.00per person</span></p>
  <p class="item" style="left:625px; top:199px;">Homemade biscuits<br>&nbsp;&nbsp;&nbsp;&nbsp;&nbsp;&nbsp;&nbsp;&nbsp;&nbsp;&nbsp;&nbsp;&nbsp;&nbsp;&nbsp;<span class="price">$4.50per person</span></p>
  <p class="item" style="left:627px; top:251px;">Banana Bread<br>&nbsp;&nbsp;&nbsp;&nbsp;<span class="price">$6.00per person</span></p>
  <p class="item" style="left:625px; top:309px;">Gluten Free frittata<br>&nbsp;&nbsp;&nbsp;&nbsp;&nbsp;&nbsp;&nbsp;&nbsp;&nbsp;&nbsp;&nbsp;&nbsp;&nbsp;&nbsp;<span class="price">$5.50per person</span></p>
  <p class="item" style="left:626px; top:365px;">Ploughmans Platter<br>&nbsp;&nbsp;&nbsp;&nbsp;&nbsp;&nbsp;&nbsp;&nbsp;&nbsp;&nbsp;&nbsp;&nbsp;&nbsp;<span class="price">$8.50per person</span></p>
  <p class="item" style="left:626px; top:421px;">Whole fresh fruit platter<br>&nbsp;&nbsp;&nbsp;&nbsp;&nbsp;&nbsp;&nbsp;&nbsp;&nbsp;&nbsp;&nbsp;&nbsp;&nbsp;<span class="price">$45.00 per platter</span></p>
  <p class="item" style="left:626px; top:478px;">Chopped fresh seasonal<br>fruit Platter<br><span class="price">$49.50 per platter</span></p>

  <!-- Platter menu -->
  <h2 class="heading" style="left:36px; width:200px; top:642px;">Platter menu</h2>
  <p class="item" style="left:27px; top:678px;">Hot finger food platter<br>(chef’s choice 60 pieces)<br>&nbsp;&nbsp;&nbsp;&nbsp;&nbsp;&nbsp;<span class="price">$105.00</span></p>
  <p class="item" style="left:25px; top:755px;">Hot roast buffet platter Pork or<br>beef with roast vegetables and<br>one grazing salad <span class="price">Minimum 10</span><br><span class="price">guests &nbsp;&nbsp;&nbsp;&nbsp;&nbsp;&nbsp;&nbsp;&nbsp;&nbsp;&nbsp;&nbsp;&nbsp;&nbsp;&nbsp;&nbsp;&nbsp;&nbsp;&nbsp;&nbsp;&nbsp;$16.50pp</span></p>
  <p class="item" style="left:25px; top:858px;">Sandwich box &nbsp;(10 rounds)<br>&nbsp;&nbsp;&nbsp;&nbsp;&nbsp;&nbsp;&nbsp;&nbsp;&nbsp;&nbsp;&nbsp;<span class="price">$68.00</span></p>
  <p class="item" style="left:29px; top:915px;">Medium bread roll platter 15<br>medium size lunch rolls<br><span class="price">$75.00</span></p>
  <p class="item" style="left:26px; top:999px;">Large meat and salad rolls<br>&nbsp;&nbsp;&nbsp;&nbsp;&nbsp;&nbsp;&nbsp;&nbsp;&nbsp;&nbsp;<span class="price">$9.00 Each</span> (choice of<br>chicken, Chicken schnitzel,</p>
  <p class="item" style="left:26px; top:1079px;">Wraps &nbsp;&nbsp;<span class="price">$7.50 &nbsp;&nbsp;Each</span> (choice<br>of chicken, Chicken schnitzel,<br>roast beef, Ham)</p>

  <!-- Salads -->
  <p class="item" style="left:323px; top:643px;">ndividual Salad Bowls<br>–Ceasar, Greek, Creamy<br>Pasta, Seafood &nbsp;&nbsp;&nbsp;&nbsp;<span class="price">$9.50</span><br>add chicken or chilled<br>chicken</p>
  <p class="item" style="left:323px; top:770px;">Large Grazing salads- add<br>one to a sandwich platter or<br>hot finger food platter add a<br>healthy side for your group<br><span class="price">(serves 10) &nbsp;&nbsp;&nbsp;&nbsp;&nbsp;&nbsp;&nbsp;&nbsp;&nbsp;&nbsp;&nbsp;&nbsp;$35.00</span></p>
  <p class="item" style="left:323px; top:903px;">Selections – Tossed green,<br>creamy pasta, Potato,<br>Ceasar, Seafood, beetroot</p>
  <p class="item" style="left:323px; top:991px;">Pizza, Pasta and salad<br><span class="price">(minimum 8 guests)</span></p>
  <div class="artwork pizza" role="img" aria-label="Illustration of a pizza with olives and capsicum"></div>

  <!-- Lunch -->
  <h2 class="heading" style="left:608px; width:200px; top:639px;">LUNCH</h2>
  <p class="heading" style="left:604px; top:674px; text-align:left; white-space:nowrap;">Gazing Table <span class="price" style="font-family:'Tinos',serif; font-size:18px; display:inline-block; transform:scaleX(0.86); transform-origin:left;">minimum 5</span></p>
  <p class="item" style="left:658px; top:702px;"><span class="price">$16.50 pp</span></p>
  <p class="item" style="left:604px; top:733px;">Make your own sandwich<br>buffet for guests to make their<br>own sandwich from a</p>
  <div class="artwork sandwich" role="img" aria-label="Illustration of a sandwich cut into triangles with tomato and lettuce"></div>

  <p class="booking">To book in your event call us Now<br>on 55 018 018 or go to<br>www.brightferncatering.com.au</p>
</main>
</body>
</html>
```